Moscato Wine Brand Graphic Design - see photos for reference and sizing guide

In need of a graphic design for our brand LUNA BELLE Pink Moscato with the following requirements:1. Pintaleon Theme - it is a popular festival in Philippines that means "many faces" and is symbolized by creative masks with vibrant colours and designs.2. We want a Pintaleon Design on our moscato bottle to represent women as Luna Belles.3. The pintaleon has to be bright,colourful, with pink,purple,musk,greys,small silver and gold stars or stripes glitter or sparkle accents to it.4. It has to have a WOW Factor, feel good label design that is aimed at Women 18yrs to 45yrs old.5. A sample is provided but feel free to play around and the most vibrant, new world design for LUNA BELLE Pink Moscato label Wins.

Target Market(s)

Women 18 to 45 yrs of age, Asian and Western Market

Font styles to use
Script

Colors

Designer to choose colors to be used in the design.

Requirements
Must have
• Bright,Bold and Vibrant Design that matches the label and it has to be a sophisticated Mask Design please refer to photo as a guide. Let your imagination run wild.
• Label Measurements: Front Label
• Width: 125mm
• Height:95mm
• Height from Base: 21mm
Nice to have
• Accents of sparkles and glitter with gold,silver,purple,pink hues or use your creativity to create a stunning mask design. The wine bottle is in Arctic Blue Sparkling Wine Bottle that makes the bottle look like light purple once the wine is in it so put it in consideration when making the label and background.

```html
<!DOCTYPE html>
<html lang="en">
<head>
<meta charset="utf-8">
<title>Luna Belle Pink Moscato – Label Print Specification</title>
<link rel="stylesheet" href="https://fonts.googleapis.com/css2?family=Great+Vibes&family=Big+Shoulders+Display:wght@300&family=Source+Sans+3:wght@400;700&family=Roboto+Condensed:ital,wght@0,300;1,300;1,400&display=swap">
<style>
  :root {
    --label-black: #231f20;
    --trim-magenta: #e5127d;
    --note-grey: #8a8a8a;
    --note-blue: #1ea7e1;
    --ink-white: #ffffff;
    --body-ink: #231f20;
    --wordmark-pink: #d24a9c;
    --silver: #c3c4c6;
    --silver-light: #e6e7e8;
  }
  * { margin: 0; padding: 0; box-sizing: border-box; }
  html, body { width: 1200px; height: 1072px; overflow: hidden; background: #ffffff; }
  .sheet { position: relative; width: 1200px; height: 1072px; font-family: "Source Sans 3", sans-serif; color: var(--body-ink); }

  .art-layer, .white-layer { position: absolute; left: 7px; width: 734px; border: 1px solid var(--trim-magenta); }
  .art-layer { top: 7px; height: 533px; background: var(--label-black); }
  .white-layer { top: 540px; height: 529px; background: var(--ink-white); }

  .mask-art { position: absolute; left: 232px; top: 28px; width: 270px; height: 293px;
    background: radial-gradient(ellipse at 50% 70%, #ffd34d 0%, #e2469c 45%, #7a4f9e 80%, rgba(35,31,32,0) 100%);
    border-radius: 50% 50% 40% 40%; }
  .mask-silhouette { position: absolute; left: 253px; top: 25px; width: 270px; height: 231px;
    background: radial-gradient(ellipse at 50% 65%, var(--silver) 0%, var(--silver-light) 60%, rgba(255,255,255,0) 100%);
    border-radius: 50% 50% 40% 40%; }

  .wordmark { position: absolute; left: 0; width: 734px; text-align: center; font-family: "Great Vibes", cursive; font-size: 84px; line-height: 1; }
  .art-layer .wordmark { top: 323px; color: var(--wordmark-pink); }
  .white-layer .wordmark { top: 318px; left: 18px; color: var(--silver); }

  .varietal { position: absolute; top: 405px; left: 0; width: 734px; text-align: center; font-family: "Big Shoulders Display", sans-serif; font-weight: 300; font-size: 31px; letter-spacing: 3px; color: var(--ink-white); }
  .volume { position: absolute; top: 466px; left: 0; width: 734px; text-align: center; font-family: "Roboto Condensed", sans-serif; font-weight: 300; font-size: 14px; line-height: 19px; letter-spacing: 1px; color: var(--ink-white); }

  .file-tag { position: absolute; left: 805px; top: 6px; font-family: "Roboto Condensed", sans-serif; font-style: italic; font-size: 24px; color: var(--trim-magenta); }
  .layer-name { position: absolute; font-family: "Roboto Condensed", sans-serif; font-style: italic; font-size: 14px; color: var(--trim-magenta); }

  .tech-copy { position: absolute; left: 766px; top: 262px; width: 430px; font-size: 23.5px; line-height: 31.8px; }
  .tech-copy h2 { font-weight: 700; font-size: 23.5px; line-height: 31.8px; }
  .tech-copy p + p { margin-top: 31.8px; }

  .callout { position: absolute; font-family: "Roboto Condensed", sans-serif; font-style: italic; font-weight: 300; font-size: 23px; line-height: 32px; }
  .callout-silver { left: 796px; top: 873px; color: var(--note-grey); }
  .callout-white { left: 805px; top: 1006px; color: var(--note-blue); }

  .guides { position: absolute; left: 0; top: 0; }
  .sheet-script { font-family: "Great Vibes", cursive; }
</style>
</head>
<body>
<main class="sheet">
  <section class="art-layer" aria-label="CMYK art layer">
    <div class="mask-art" role="img" aria-label="Ornate festival mask headdress in pink, purple and gold with dotted accents"></div>
    <div class="wordmark">Luna Belle</div>
    <div class="varietal">PINK MOSCATO</div>
    <div class="volume">0.75L<br>13% ALC.</div>
  </section>

  <section class="white-layer" aria-label="White ink layer">
    <div class="mask-silhouette" role="img" aria-label="Silver mask headdress area left free of white ink"></div>
    <div class="wordmark">Luna Belle</div>
  </section>

  <div class="file-tag">4cp Art File</div>
  <span class="layer-name" style="left:1086px; top:52px;">CMYK Layer</span>
  <span class="layer-name" style="left:1100px; top:117px;">White Layer</span>
  <span class="layer-name" style="left:1111px; top:189px;">Silver Substrate</span>

  <div class="tech-copy">
    <h2>Technical Description:</h2>
    <p>4cp Art Layer - printed on a Silver<br>Substrate. Combined with a White Ink<br>layer that prints on the substrate<br>first (shown below), then the CMYK art<br>file on top of that.</p>
    <p>Resulting in a Matte look for all the<br>elements on the 4cp art layer in those<br>sections. Any area that there is no<br>white ink printed, the 4cp<br>elements from the art layer will<br>appear bright/shinning from the silver<br>substrate beneath it. Really making<br>the colorful sections of this design-<br>POP and really seperate the wine<br>bottle from the rest on the shelf.</p>
  </div>

  <div class="callout callout-silver">No White Ink applied<br>showing where silver stock appears</div>
  <div class="callout callout-white">Everything showing as white is where<br>Whit Ink is applied</div>

  <svg class="guides" width="1200" height="1072" viewBox="0 0 1200 1072" aria-hidden="true">
    <defs>
      <marker id="head-magenta" markerWidth="8" markerHeight="8" refX="1" refY="4" orient="auto"><path d="M8 1 L1 4 L8 7" fill="none" stroke="#e5127d" stroke-width="1.2"/></marker>
      <marker id="head-grey" markerWidth="8" markerHeight="8" refX="1" refY="4" orient="auto"><path d="M8 1 L1 4 L8 7" fill="none" stroke="#7d7d7d" stroke-width="1.2"/></marker>
      <marker id="head-blue" markerWidth="8" markerHeight="8" refX="1" refY="4" orient="auto"><path d="M8 1 L1 4 L8 7" fill="none" stroke="#1ea7e1" stroke-width="1.2"/></marker>
      <linearGradient id="silver-foil" x1="0" y1="0" x2="1" y2="0.3">
        <stop offset="0" stop-color="#f2f2f3"/>
        <stop offset="0.3" stop-color="#b9babd"/>
        <stop offset="0.55" stop-color="#eeeeef"/>
        <stop offset="0.75" stop-color="#a7a8ab"/>
        <stop offset="1" stop-color="#d9dadc"/>
      </linearGradient>
      <linearGradient id="white-sheet" x1="0" y1="0" x2="0" y2="1">
        <stop offset="0" stop-color="#ffffff"/>
        <stop offset="1" stop-color="#ececed"/>
      </linearGradient>
    </defs>

    <g class="layer-stack">
      <polygon class="stack-silver" points="768,168 900,237 1130,228 1082,181" fill="url(#silver-foil)"/>
      <polygon class="stack-white" points="770,163 1055,118 1143,166 890,216" fill="url(#white-sheet)" stroke="#d8d8da" stroke-width="0.8"/>
      <text class="sheet-script" x="925" y="190" font-size="22" fill="#9c9d9f" transform="rotate(-12 925 190)">Luna Belle</text>
      <polygon class="stack-cmyk" points="762,158 1008,57 1132,87 904,189" fill="#231f20" stroke="#e5127d" stroke-width="1.5"/>
      <text class="sheet-script" x="918" y="150" font-size="20" fill="#b06bb0" transform="rotate(-22 918 150)">Luna Belle</text>
    </g>

    <line x1="216" y1="426" x2="279" y2="426" stroke="#ffffff" stroke-width="1.5" stroke-dasharray="1.5 2"/>
    <line x1="466" y1="426" x2="529" y2="426" stroke="#ffffff" stroke-width="1.5" stroke-dasharray="1.5 2"/>
    <line x1="796" y1="21" x2="757" y2="24" stroke="#e5127d" stroke-width="1.2" marker-end="url(#head-magenta)"/>
    <line x1="783" y1="889" x2="462" y2="760" stroke="#7d7d7d" stroke-width="1" marker-end="url(#head-grey)"/>
    <line x1="783" y1="889" x2="533" y2="899" stroke="#7d7d7d" stroke-width="1" marker-end="url(#head-grey)"/>
    <line x1="789" y1="1018" x2="539" y2="1026" stroke="#1ea7e1" stroke-width="1" marker-end="url(#head-blue)"/>
  </svg>
</main>
</body>
</html>
```